Visitenkarten-Design für Fotograf gesucht
Zielgruppe
Ich bin Fotograf der ein step in Richtung Professionalität wagen möchte.
Aufgabenstellung
Ich habe bereits ein Logo welches ich als Datei angefügt habe.
Ich hatte überlegt gehabt eine Art Prägung im Design zu haben bzw. in der Visitenkarte, eventuell das Kamera Zeichen in meinem Logo. Sonst bin ich relativ offen.
Eine weitere Überlegung ist eine eher kontrastreiche Karte haben könnte, eventuell die Rückseite dunkelgrau oder schwarz.
Es kann wenn man eine dritte Farbe hinzufügen möchte ein mittleres bis dunkles Rot hinzufügen.
Ich habe ein paar Designs hinzugefügt die mir sehr zugesagt haben.
Ansonsten bin ich auch für ein Design in der kompletten Gegenteiligkeit offen.

```html
<!DOCTYPE html>
<html lang="de">
<head>
<meta charset="utf-8">
<title>Mirko Trell Photography – Visitenkarte</title>
<link href="https://fonts.googleapis.com/css2?family=Open+Sans:wght@300;400&display=swap" rel="stylesheet">
<style>
  :root {
    --stage: #e4e4e4;
    --card-white: #ffffff;
    --ink: #111111;
    --charcoal: #3a3534;
    --hairline: #cfc9c7;
    --accent-red: #b3121b;
    --text-grey: #333333;
  }
  * { box-sizing: border-box; margin: 0; padding: 0; }
  html, body { width: 1200px; height: 800px; overflow: hidden; }
  body {
    background: var(--stage);
    font-family: "Open Sans", Arial, sans-serif;
    display: flex;
    align-items: center;
    justify-content: center;
    gap: 60px;
  }
  .card {
    position: relative;
    width: 520px;
    height: 298px;
    background: var(--card-white);
    box-shadow: 0 6px 22px rgba(0,0,0,.18);
    overflow: hidden;
  }

  /* Back side */
  .card-back .dark-band {
    position: absolute;
    left: 0; top: 0;
    width: 100%;
    height: 160px;
    background: var(--charcoal);
  }
  .card-back .band-rule {
    position: absolute;
    left: 0; right: 0;
    top: 130px;
    height: 1px;
    background: var(--hairline);
    opacity: .7;
  }
  .card-back .brand-name {
    position: absolute;
    left: 0; right: 0;
    top: 40px;
    text-align: center;
    color: var(--card-white);
    font-weight: 300;
    font-size: 38px;
    line-height: 1.2;
    letter-spacing: 1px;
  }
  .card-back .brand-tag {
    position: absolute;
    left: 0; right: 0;
    top: 96px;
    text-align: center;
    color: var(--card-white);
    font-weight: 300;
    font-size: 9px;
    letter-spacing: 4px;
  }
  .card-back .contact {
    position: absolute;
    left: 0; right: 0;
    top: 176px;
    text-align: center;
    color: var(--text-grey);
    font-size: 14px;
    line-height: 1.5;
  }
  .card-back .contact .dot {
    display: inline-block;
    width: 6px; height: 6px;
    border-radius: 50%;
    background: var(--accent-red);
    margin: 0 9px;
    vertical-align: middle;
  }
  .card-back .foot-rule {
    position: absolute;
    left: 0; right: 0;
    bottom: 30px;
    height: 1px;
    background: var(--ink);
    opacity: .5;
  }

  /* Front side */
  .card-front .brand-square {
    position: absolute;
    left: 62px;
    top: 131px;
    width: 36px;
    height: 36px;
    background: var(--ink);
  }
  .card-front .divider {
    position: absolute;
    left: 112px;
    top: 52px;
    width: 1px;
    height: 190px;
    background: var(--ink);
  }
  .card-front .brand-block {
    position: absolute;
    left: 150px;
    right: 50px;
    top: 112px;
    text-align: right;
  }
  .card-front .brand-name {
    color: var(--ink);
    font-weight: 300;
    font-size: 44px;
    line-height: 1.1;
    letter-spacing: 1px;
    text-align: center;
  }
  .card-front .brand-tag {
    margin-top: 8px;
    color: var(--ink);
    font-weight: 300;
    font-size: 10px;
    letter-spacing: 5px;
  }
</style>
</head>
<body>

  <section class="card card-back" aria-label="Rückseite">
    <div class="dark-band"></div>
    <p class="brand-name">Mirko Trell</p>
    <p class="brand-tag">PHOTOGRAPHY</p>
    <div class="band-rule"></div>
    <p class="contact">
      lindenweg 48<span class="dot"></span>31795 feldhausen<br>
      +49 512 830 264<span class="dot"></span>+49 176 402 918<br>
      info@mt-photography.de
    </p>
    <div class="foot-rule"></div>
  </section>

  <section class="card card-front" aria-label="Vorderseite">
    <div class="brand-square"></div>
    <div class="divider"></div>
    <div class="brand-block">
      <p class="brand-name">Mirko Trell</p>
      <p class="brand-tag">PHOTOGRAPHY</p>
    </div>
  </section>

</body>
</html>
```